Fleet Service Tri Fold Flyer

I am looking to come up with a flyer design to hand out showing our services. I will upload more info with working, but in the mean time want to just have a flyer to pass out. I have uploaded our logo and the images for it. I also uploaded what our trucks look like for ideas, as well as a business card.

Industry/Entity Type

Mobile Hydraulics and Fleet Service

Colors
0054AA
0677BA
7BADD7
CADEEF
E8F1F8
F0912C
F2A743
F7CA91
FBE8D2
FDF5EE

Requirements
Must have
• I uploaded a PDF with wording for the flyer

```html
<!DOCTYPE html>
<html lang="en">
<head>
<meta charset="utf-8">
<title>Readyline Fleet Service Flyer</title>
<link href="https://fonts.googleapis.com/css2?family=Montserrat:wght@300;400;600;700;800&family=Arimo:wght@400;700&display=swap" rel="stylesheet">
<style>
:root{
  --blue-deep:#0054AA;
  --blue:#0677BA;
  --blue-soft:#7BADD7;
  --blue-pale:#CADEEF;
  --blue-mist:#E8F1F8;
  --orange:#F0912C;
  --orange-light:#F2A743;
  --orange-soft:#F7CA91;
  --ink:#333840;
  --slate:#4a4a4c;
  --white:#ffffff;
}
*{margin:0;padding:0;box-sizing:border-box}
html,body{width:800px;height:1200px;overflow:hidden;background:#fff}
.flyer{position:relative;width:800px;height:1200px;background:#fff;font-family:"Arimo",Arial,sans-serif;color:var(--ink);overflow:hidden}
.hero-bg{position:absolute;left:0;top:0;width:800px;height:520px;background:linear-gradient(135deg,#fafafa 0%,#f0f1f3 55%,#e6e8eb 100%)}
.frame{position:absolute;left:0;top:0}
.brand{position:absolute;left:48px;top:52px;display:flex;align-items:center;gap:8px;font-family:"Montserrat",sans-serif;font-weight:800;font-size:19px;color:var(--blue-deep);letter-spacing:.5px}
.brand-mark{width:14px;height:14px;background:var(--orange)}
.truck-photo{position:absolute;left:255px;top:150px;width:545px;height:320px;border-radius:40px 0 0 0;background:linear-gradient(160deg,#f4f6f9 0%,var(--blue-pale) 45%,var(--blue) 100%)}
.headline{position:absolute;left:28px;top:195px;font-family:"Montserrat",sans-serif;line-height:1.05}
.headline .l1{font-weight:300;font-size:30px;color:var(--ink)}
.headline .l2{font-weight:700;font-size:30px;color:var(--blue)}
.headline .l3{font-weight:400;font-size:22px;color:var(--ink);margin-top:2px}
.about{position:absolute;left:28px;top:325px;width:215px}
.about h3{font-family:"Montserrat",sans-serif;font-weight:700;font-size:14px;margin-bottom:14px}
.about p{font-size:10.5px;line-height:1.35;color:#3a3a3a}
.services-panel{position:absolute;left:30px;top:620px;width:745px;height:168px;border-radius:14px;background:linear-gradient(180deg,var(--blue) 0%,var(--blue-deep) 100%)}
.service{position:absolute;top:585px;width:150px;text-align:center}
.service .icon{width:76px;height:76px;margin:0 auto;border-radius:50%;background:var(--orange);border:3px solid var(--orange-soft);display:flex;align-items:center;justify-content:center}
.service .label{margin-top:24px;color:#fff;font-weight:700;font-size:16px;line-height:1.3}
.divider{position:absolute;top:640px;height:130px;border-left:1.5px dashed var(--blue-soft)}
.tasks-title{position:absolute;left:30px;top:810px;font-family:"Montserrat",sans-serif;font-weight:800;font-size:20px;line-height:1.2}
.tasks-title .accent{color:var(--orange)}
.tasks-title .dark{color:var(--ink)}
.tasks{position:absolute;left:38px;top:0;width:450px;list-style:none}
.tasks li{position:absolute;left:0;width:450px;display:flex;gap:22px;font-size:11.5px;line-height:1.4;align-items:flex-start}
.tasks li span{width:410px}
.tasks svg{flex:none;margin-top:1px}
.mechanic-art{position:absolute;left:505px;top:830px;width:240px;height:265px;border-radius:50%;background:radial-gradient(circle at 50% 45%,var(--blue-pale) 0%,var(--blue-mist) 60%,#fff 100%)}
.footer-strip{position:absolute;left:0;top:1110px}
.contact{position:absolute;color:#fff;font-size:10px}
.contact-name{left:30px;top:1120px}
.contact-name .name{color:var(--orange);font-family:"Montserrat",sans-serif;font-size:13px}
.contact-name .role{font-size:9px;font-weight:700}
.contact-line{display:flex;align-items:center;gap:6px;margin-top:4px}
.contact-web{left:275px;top:1120px}
.contact-web .phone{font-family:"Montserrat",sans-serif;font-size:16px;font-weight:600;margin-top:0}
.address{position:absolute;left:580px;top:1128px;display:flex;gap:10px;font-size:11px;line-height:1.3;color:var(--ink)}
</style>
</head>
<body>
<main class="flyer">
  <div class="hero-bg"></div>

  <div class="truck-photo" role="img" aria-label="Photo of a white and blue service van with the company name, 24 hours badge and phone number on its side"></div>

  <svg class="frame" width="800" height="520" viewBox="0 0 800 520" aria-hidden="true">
    <polygon points="340,28 800,28 800,44 330,44" fill="var(--blue-deep)"/>
    <polygon points="250,115 320,40 348,40 275,122" fill="var(--orange)"/>
    <polygon points="268,132 350,50 800,50 800,56 356,56 282,132" fill="var(--orange)"/>
    <rect x="0" y="110" width="262" height="6" fill="var(--orange)"/>
    <polygon points="0,122 255,122 244,140 0,140" fill="var(--blue)"/>
    <polygon points="0,470 800,470 800,480 0,480" fill="var(--orange)"/>
    <polygon points="0,480 440,480 470,500 800,500 800,505 0,505" fill="var(--blue-deep)"/>
    <polygon points="455,480 800,480 800,500 475,500" fill="var(--orange-light)"/>
  </svg>

  <div class="brand"><span class="brand-mark"></span>READYLINE FLEET SERVICE</div>

  <h1 class="headline">
    <div class="l1">MOBILE FLEET</div>
    <div class="l2">SERVICE AND REPAIR</div>
    <div class="l3">AT YOUR YARD OR JOB SITE</div>
  </h1>

  <section class="about">
    <h3>About Us</h3>
    <p>Mobile Hose Repair Service, 24/7, 365 Days, specializing in reducing customer's equipment downtime and operating cost, by coming to you with a fully stocked truck and a mobile workshop.</p>
  </section>

  <div class="services-panel"></div>
  <div class="divider" style="left:180px"></div>
  <div class="divider" style="left:325px"></div>
  <div class="divider" style="left:480px"></div>
  <div class="divider" style="left:625px"></div>

  <div class="service" style="left:30px">
    <div class="icon"><svg width="40" height="40" viewBox="0 0 40 40" fill="none" stroke="#fff" stroke-width="2.5"><path d="M5 24 l4-9 h16 l4 9 v7 H5z"/><circle cx="11" cy="31" r="3" fill="#fff"/><circle cx="23" cy="31" r="3" fill="#fff"/><path d="M30 8 l6 26"/></svg></div>
    <div class="label">Mobile<br>Hydraulic<br>Repair</div>
  </div>
  <div class="service" style="left:178px">
    <div class="icon"><svg width="40" height="40" viewBox="0 0 40 40" fill="none" stroke="#fff" stroke-width="2.5"><circle cx="20" cy="12" r="6"/><rect x="9" y="22" width="22" height="12" rx="2"/><path d="M5 34 h30"/></svg></div>
    <div class="label">We come<br>to you</div>
  </div>
  <div class="service" style="left:328px">
    <div class="icon"><svg width="40" height="40" viewBox="0 0 40 40" fill="none" stroke="#fff" stroke-width="3"><circle cx="20" cy="20" r="15"/><circle cx="20" cy="22" r="4"/><path d="M6 18 h10 M24 18 h10 M20 26 v9"/></svg></div>
    <div class="label">Complete<br>Lube service,<br>oil changes,<br>brake service</div>
  </div>
  <div class="service" style="left:478px">
    <div class="icon"><svg width="40" height="40" viewBox="0 0 40 40" fill="none" stroke="#fff" stroke-width="3"><circle cx="15" cy="15" r="8"/><circle cx="15" cy="15" r="3"/><path d="M21 21 l12 12"/></svg></div>
    <div class="label">Roadside<br>Assistance</div>
  </div>
  <div class="service" style="left:625px">
    <div class="icon"><svg width="40" height="40" viewBox="0 0 40 40" fill="none" stroke="#fff" stroke-width="3"><rect x="6" y="8" width="24" height="18" rx="2"/><path d="M18 26 v6 M11 33 h14"/><rect x="31" y="10" width="4" height="22"/></svg></div>
    <div class="label">Advanced<br>Computer</div>
  </div>

  <h2 class="tasks-title"><span class="accent">THE SERVICES OUR</span><br><span class="dark">TECHNICIAN WILL PROVIDE</span></h2>

  <ul class="tasks">
    <li style="top:884px"><svg width="18" height="18" viewBox="0 0 18 18" fill="none" stroke="var(--blue)" stroke-width="2"><rect x="1" y="3" width="14" height="14"/><path d="M4 9 l4 4 l9-11"/></svg><span>Quickley assess the situation and failure.</span></li>
    <li style="top:914px"><svg width="18" height="18" viewBox="0 0 18 18" fill="none" stroke="var(--blue)" stroke-width="2"><rect x="1" y="3" width="14" height="14"/><path d="M4 9 l4 4 l9-11"/></svg><span>We will remove the failed hose to use it as a template to make a new one.</span></li>
    <li style="top:962px"><svg width="18" height="18" viewBox="0 0 18 18" fill="none" stroke="var(--blue)" stroke-width="2"><rect x="1" y="3" width="14" height="14"/><path d="M4 9 l4 4 l9-11"/></svg><span>The Truck is fully equipped to be able to custom fabricate a replacement hose to match exactly what you need.</span></li>
    <li style="top:1012px"><svg width="18" height="18" viewBox="0 0 18 18" fill="none" stroke="var(--blue)" stroke-width="2"><rect x="1" y="3" width="14" height="14"/><path d="M4 9 l4 4 l9-11"/></svg><span>We will then install the custom made hydraulic hose assembly on site without you ever having to move or transport the machine.</span></li>
    <li style="top:1060px"><svg width="18" height="18" viewBox="0 0 18 18" fill="none" stroke="var(--blue)" stroke-width="2"><rect x="1" y="3" width="14" height="14"/><path d="M4 9 l4 4 l9-11"/></svg><span>We will then work with the customer to ensure the equipment is up and running before leaving the jobsite.</span></li>
  </ul>

  <div class="mechanic-art" role="img" aria-label="Illustration of a mechanic holding a large wrench beside an orange car, with gears and a tools sign"></div>

  <svg class="footer-strip" width="800" height="90" viewBox="0 0 800 90" aria-hidden="true">
    <polygon points="0,4 530,4 495,70 0,70" fill="var(--slate)"/>
    <polygon points="500,68 800,68 800,90 488,90" fill="var(--orange)"/>
  </svg>

  <div class="contact contact-name">
    <div class="name">DANIEL HARLOW</div>
    <div class="role">MANAGER</div>
    <div class="contact-line"><svg width="11" height="9" viewBox="0 0 11 9" fill="none" stroke="var(--orange)"><rect x=".5" y=".5" width="10" height="8"/><path d="M.5 .5 l5 4 l5-4"/></svg>daniel@readylinerentals.com</div>
  </div>

  <div class="contact contact-web">
    <div class="contact-line phone"><svg width="13" height="13" viewBox="0 0 13 13" fill="var(--orange)"><path d="M3 1 l2 3 l-1 1.5 q1.5 3 4 4 l1.5-1 l3 2 l-1 2 q-6 0-11-6 q-.5-3 2.5-5.5z"/></svg>555-014-2290</div>
    <div class="contact-line"><svg width="12" height="12" viewBox="0 0 12 12" fill="none" stroke="var(--orange)"><circle cx="6" cy="6" r="5"/><path d="M1 6 h10 M6 1 q-3 5 0 10 M6 1 q3 5 0 10"/></svg>www.readylinerentals.com</div>
  </div>

  <div class="address">
    <svg width="12" height="16" viewBox="0 0 12 16" fill="var(--orange)"><path d="M6 0 a6 6 0 0 1 6 6 c0 4-6 10-6 10 S0 10 0 6 a6 6 0 0 1 6-6z"/><circle cx="6" cy="6" r="2" fill="#fff"/></svg>
    <span>4120 Harbor Mill Road,<br>Lakeview FL 34000</span>
  </div>
</main>
</body>
</html>
```